Ravelor Global Kft. is an online recruitment marketplace connecting the employers and recruiters together. We provide an e-bussiness solution for companies and give busines opportunity for recruiters.
We have a logo design already, which should be used on the business card.
Our colours are grey and magenta, which can be seen in the logo. Black is also welcome.
The style should be dynamic, young but professional. It should be clear, visible, elegant, not too crowded, simple but exciting.
We need the following data on the BC: name, title, address, phone,fax and mobile number, email address, website.
Target Market(s)
Our target market are companies, as this is a B2B business. We also target recruiters, recruitment professionals, headhunters.We would like to be impressive and different.
Industry/Entity Type
Business
Requirements
Must have
- We would like to promote our website, www.ravelorglb.hu.
- Please, put this on the back with a quite visible letter size.The style should be dynamic, young but professional. It should be clear, visible, elegant, not too crowded, simple but exciting.
Should not have
- We do not want to see people figures.

```html
<!DOCTYPE html>
<html lang="en">
<head>
<meta charset="utf-8">
<title>Ravelor Global Kft. – Business Card</title>
<link rel="stylesheet" href="https://fonts.googleapis.com/css2?family=Oswald:wght@700&family=Arimo:wght@400;700&display=swap">
<style>
  :root {
    --magenta: #b5196e;
    --grey: #857284;
    --grey-text: #8a7b8c;
    --paper: #ffffff;
  }
  html, body {
    margin: 0;
    padding: 0;
    overflow: hidden;
    background: var(--paper);
  }
  .card {
    position: relative;
    width: 1200px;
    height: 800px;
    background: var(--paper);
    overflow: hidden;
    font-family: "Arimo", Arial, sans-serif;
  }
  .brand-mark {
    position: absolute;
    left: 0;
    top: 0;
    width: 290px;
    height: 287px;
    background: var(--magenta);
  }
  .brand-name {
    position: absolute;
    left: 312px;
    top: 132px;
    margin: 0;
    font-family: "Oswald", "Arial Narrow", sans-serif;
    font-weight: 700;
    font-size: 150px;
    line-height: 1;
    color: var(--magenta);
    letter-spacing: 2px;
  }
  .person-name {
    position: absolute;
    left: 320px;
    top: 316px;
    margin: 0;
    font-weight: 700;
    font-size: 44px;
    letter-spacing: 3px;
    color: var(--grey);
  }
  .contact {
    position: absolute;
    left: 0;
    width: 1190px;
    top: 664px;
    margin: 0;
    text-align: center;
    font-size: 29px;
    line-height: 43px;
    color: var(--grey-text);
  }
  .web-band {
    position: absolute;
    left: 0;
    bottom: 0;
    width: 1200px;
    height: 45px;
    background: var(--magenta);
    color: var(--paper);
    font-size: 28px;
    line-height: 45px;
    text-align: center;
    letter-spacing: 1px;
    text-indent: -20px;
  }
</style>
</head>
<body>
  <main class="card">
    <div class="brand-mark" aria-hidden="true"></div>
    <h1 class="brand-name">RAVELOR</h1>
    <p class="person-name">Varga Eszter</p>
    <p class="contact">
      Head Office: 72, Orchard Vale St, Budapest.<br>
      Telefax: 77731946, E-mail: sales@Ravelor.com
    </p>
    <div class="web-band">WWW.RAVELORGLB.HU</div>
  </main>
</body>
</html>
```